Building Maintenance Flyer specialising in hot and silent pressure cleaning

Hi. I love this flyer. I would like something similar but with hot water pressure washing and building maintenance

Ferro Lane & Services provides high pressure steam cleaning and water blasting services throughout Brisbane and surrounding areas, covering the Industrial, Commercial, Strata and Residential property owners sectors.

FLS combining the cleaning power of heat with state-of-the-art silent equipment, accredited technicians and a steadfast commitment to the environment. We offer the best Prompt, Professional Service.

Fully Accredited & Certified Technicians
100% Satisfaction Guaranteed
We are a family owned and operated business and love what we do. No job is too big or too small and we take pride in our work.
All of our services are undertaken using industry leading equipment and, providing safe and superior results.

Our business is covered by 20 million full public liability insurance and we operate within strict health & safety guidelines, providing all our clients with complete peace of mind. Project plans and risk assessments can also be provided upon request.

BODY CORPORATES

BUILDING FAÇADE CLEANING

CAR PARKS – underground, single and multi level

DRIVE THRU

FOOD PRODUCTION FACILITIES CLEANING SANITISING

SHOPPING CENTRES

BIRD MANAGEMENT AND DECONTAMINATION

GENERAL MAINTENANCE

CONSTRUCTION CLEAN UPS

SPILL MANAGEMENT

CONCRETE CLEANING AND DEGRASING

CONCRETE SEALING

FACTORY CLEANING & CLEAN UP

ENVIRONMENTAL DECONTAMINATION OF HEAVY VEHICLES AND EQUIPMENT

SITE CLEANS AND RUBBISH REMOVAL

MANUFACTURING PLANTS

Target Market(s)

Facility Managers, Commercial and Industrial Property Owners, Property Managers, Schools, Restaurants,

Industry/Entity Type

Pressure Cleaning

Font styles to use
Sans Serif

Colors
0293ce
00a990
33a6d7
33b8a4

Requirements
Must have
• SILENT HOT WATER PRESSURE CLEANING
Runs up to 120 Degrees Celsius
SANITISING - Bin areas, outdoor areas, cafe's, restaurants, schools, drive thru's
Blue's and Greens to link in with our logo

```html
<!DOCTYPE html>
<html lang="en">
<head>
<meta charset="utf-8">
<title>Ferro Lane &amp; Services – Property Maintenance Flyer</title>
<link rel="stylesheet" href="https://fonts.googleapis.com/css2?family=Roboto+Condensed:wght@700&family=Montserrat:wght@400;600;700&display=swap">
<style>
  :root{
    --teal:#1ea7a8;
    --blue:#0293ce;
    --blue-2:#2a6fbe;
    --navy:#1c4d8c;
    --paper-grey:#e3e3e4;
    --white:#ffffff;
    --ink:#3d3d3d;
    --ink-soft:#555555;
    --band:#5a5a5c;
    --gold-dark:#b8871d;
    --page:#ececec;
  }
  *{margin:0;padding:0;box-sizing:border-box}
  html,body{width:714px;height:1200px;overflow:hidden;background:var(--page)}
  .canvas{position:relative;width:714px;height:1200px}
  .flyer{
    position:absolute;left:12px;top:134px;width:599px;height:808px;
    transform:scale(1.152);transform-origin:0 0;
    background:var(--paper-grey);overflow:hidden;
    box-shadow:0 2px 6px rgba(0,0,0,.18);
    font-family:"Montserrat",Arial,sans-serif;color:var(--ink);
  }
  .shapes{position:absolute;inset:0}
  .headline{position:absolute;left:38px;top:40px;font-family:"Roboto Condensed","Arial Narrow",sans-serif;font-weight:700;line-height:1.02}
  .headline .line{display:block;font-size:33px;color:var(--teal)}
  .headline .line--strong{color:var(--navy);font-size:35px;margin-top:4px}
  .intro{position:absolute;left:38px;top:170px;width:210px;padding-left:10px;border-left:1.5px solid #777;font-size:10.3px;line-height:12.8px;color:var(--ink)}
  .accredited{position:absolute;left:38px;top:282px;font-family:"Roboto Condensed","Arial Narrow",sans-serif;font-weight:700;font-size:23px;line-height:25px;color:var(--ink-soft)}
  .feature{position:absolute;left:38px;display:flex;align-items:center;gap:22px}
  .feature__icon{width:56px;height:56px;flex:none}
  .feature__text{font-weight:700;font-size:12px;line-height:14px;color:var(--ink)}
  .solutions-title{position:absolute;left:328px;top:372px;font-family:"Roboto Condensed","Arial Narrow",sans-serif;font-weight:700;font-size:19px;color:var(--blue-2)}
  .solutions-list{position:absolute;top:412px;list-style:none;width:118px}
  .solutions-list--a{left:328px}
  .solutions-list--b{left:451px}
  .solutions-list li{position:relative;padding-left:10px;font-size:6.3px;font-weight:600;line-height:7.6px;color:#333;margin-bottom:6.6px}
  .solutions-list li::before{content:"";position:absolute;left:0;top:1px;width:5px;height:5px;border:.8px solid var(--blue-2)}
  .follow{position:absolute;left:300px;top:662px;font-family:"Roboto Condensed","Arial Narrow",sans-serif;font-weight:700;font-size:10.5px;line-height:11px;color:#333}
  .social{position:absolute;left:382px;top:668px;display:flex;gap:7px}
  .social span{width:11px;height:11px;border-radius:50%;background:var(--teal)}
  .brand{position:absolute;left:468px;top:650px;display:flex;align-items:center;gap:6px;font-family:"Montserrat",Arial,sans-serif;font-weight:700;font-size:26px;color:var(--blue-2)}
  .brand__dot{width:12px;height:12px;border-radius:50%;background:var(--blue-2)}
  .contact{position:absolute;left:306px;top:720px;color:var(--white)}
  .contact__row{display:flex;align-items:center;gap:12px}
  .contact__phone{font-weight:600;font-size:27px;letter-spacing:.5px;line-height:34px}
  .contact__web{font-weight:600;font-size:16px;letter-spacing:2.4px;line-height:26px}
  .contact svg{width:18px;height:18px;flex:none}
</style>
</head>
<body>
<div class="canvas">
  <section class="flyer" aria-label="Ferro Lane &amp; Services property maintenance flyer">
    <svg class="shapes" width="599" height="808" viewBox="0 0 599 808">
      <defs>
        <linearGradient id="swoosh" x1="0" y1="0" x2="1" y2="1">
          <stop offset="0" stop-color="#1ab3b0"/>
          <stop offset=".55" stop-color="#2c7fc6"/>
          <stop offset="1" stop-color="#2461b5"/>
        </linearGradient>
        <linearGradient id="photoTop" x1="0" y1="0" x2="1" y2="1">
          <stop offset="0" stop-color="#d7dde3"/>
          <stop offset=".5" stop-color="#8ea0b3"/>
          <stop offset="1" stop-color="#2d3f86"/>
        </linearGradient>
        <linearGradient id="photoBottom" x1="0" y1="0" x2="1" y2="1">
          <stop offset="0" stop-color="#e6e9ec"/>
          <stop offset=".5" stop-color="#3550a6"/>
          <stop offset="1" stop-color="#cfd3d7"/>
        </linearGradient>
        <radialGradient id="gold" cx=".4" cy=".35" r=".7">
          <stop offset="0" stop-color="#f6dc7c"/>
          <stop offset="1" stop-color="#c58f1f"/>
        </radialGradient>
      </defs>
      <rect x="0" y="263" width="300" height="300" fill="var(--white)"/>
      <path d="M470 0 C360 40 268 170 288 262 C308 334 430 350 599 238 L599 0 Z" fill="url(#swoosh)"/>
      <path d="M485 0 C390 60 330 160 352 225 C378 292 480 298 599 232 L599 0 Z" fill="url(#photoTop)" role="img" aria-label="Photo: technician in blue overalls and yellow gloves tightening a valve with a wrench"/>
      <rect x="262" y="632" width="337" height="80" fill="var(--white)"/>
      <path d="M272 710 L599 710 L599 808 L262 808 Q262 752 272 710 Z" fill="var(--band)"/>
      <path d="M0 566 Q150 536 228 598 Q268 650 262 808 L0 808 Z" fill="url(#photoBottom)" role="img" aria-label="Photo: technician in blue uniform with tool belt carrying a toolbox beside a van"/>
      <path d="M0 566 Q150 536 228 598 Q268 650 262 808" fill="none" stroke="var(--navy)" stroke-width="5"/>
      <circle cx="224" cy="593" r="68" fill="var(--gold-dark)"/>
      <circle cx="224" cy="593" r="62" fill="url(#gold)"/>
      <circle cx="224" cy="593" r="40" fill="none" stroke="var(--gold-dark)" stroke-width="2"/>
    </svg>

    <h1 class="headline">
      <span class="line">All commercial &amp;</span>
      <span class="line">Industial property</span>
      <span class="line line--strong">Maintenance</span>
    </h1>
    <p class="intro">We combining the cleaning power of heat with state-of-the-art silent equipment, accredited technicians and a steadfast commitment to the environment. We offer the best Prompt, Professional Service.</p>

    <h2 class="accredited">Fully Accredited<br>&amp; Certified Technicians</h2>

    <div class="feature" style="top:344px">
      <svg class="feature__icon" viewBox="0 0 56 56"><circle cx="28" cy="28" r="28" fill="var(--blue)"/><circle cx="28" cy="28" r="13" fill="none" stroke="#fff" stroke-width="2"/><path d="M28 20v8l6 4" fill="none" stroke="#fff" stroke-width="2" stroke-linecap="round"/></svg>
      <p class="feature__text">We operate 24/7,<br>7 days a week</p>
    </div>
    <div class="feature" style="top:410px">
      <svg class="feature__icon" viewBox="0 0 56 56"><circle cx="28" cy="28" r="28" fill="var(--blue)"/><path d="M28 14 C22 23 19 28 19 32 a9 9 0 0 0 18 0 C37 28 34 23 28 14 Z" fill="none" stroke="#fff" stroke-width="2"/></svg>
      <p class="feature__text">Silent hot water pressure<br>cleaning up to 120°C<br>&amp; sanitising</p>
    </div>
    <div class="feature" style="top:474px">
      <svg class="feature__icon" viewBox="0 0 56 56"><circle cx="28" cy="28" r="28" fill="var(--blue)"/><path d="M28 14 L39 18 V28 C39 35 34 40 28 42 C22 40 17 35 17 28 V18 Z" fill="none" stroke="#fff" stroke-width="2"/><path d="M23 28 l4 4 l7 -8" fill="none" stroke="#fff" stroke-width="2" stroke-linecap="round"/></svg>
      <p class="feature__text">COVID-19<br>Trained</p>
    </div>

    <h2 class="solutions-title">Solutions For</h2>
    <ul class="solutions-list solutions-list--a">
      <li>Construction Clean Ups</li>
      <li>Spill Management</li>
      <li>Concrete Cleaning And Degrasing</li>
      <li>Concrete Sealing</li>
      <li>Factory Cleaning &amp; Clean Up</li>
      <li>Environmental Decontamination Of Heavy Vehicles And Equipment</li>
      <li>Site Cleans And Rubbish Removal</li>
      <li>Manufacturing Plants</li>
    </ul>
    <ul class="solutions-list solutions-list--b">
      <li>Body Corporates</li>
      <li>Building Façade Cleaning</li>
      <li>Car Parks - Underground Single And Multi Level</li>
      <li>Drive Thru</li>
      <li>Food Production Facilities Cleaning Sanitising</li>
      <li>Shopping Centres</li>
      <li>Bird Management And Decontamination</li>
      <li>General Maintenance</li>
    </ul>

    <p class="follow">Follow us on<br>social media</p>
    <div class="social" aria-hidden="true"><span></span><span></span><span></span></div>
    <div class="brand"><span class="brand__dot"></span>FLS</div>

    <div class="contact">
      <div class="contact__row">
        <svg viewBox="0 0 24 24"><path d="M6.6 10.8a15 15 0 0 0 6.6 6.6l2.2-2.2c.3-.3.7-.4 1-.2 1.1.4 2.3.6 3.6.6.6 0 1 .4 1 1V20c0 .6-.4 1-1 1C10.6 21 3 13.4 3 4c0-.6.4-1 1-1h3.5c.6 0 1 .4 1 1 0 1.3.2 2.5.6 3.6.1.3 0 .7-.2 1Z" fill="#fff"/></svg>
        <span class="contact__phone">0400 555 018</span>
      </div>
      <div class="contact__row">
        <svg viewBox="0 0 24 24" fill="none" stroke="#fff" stroke-width="1.6"><circle cx="12" cy="12" r="9"/><ellipse cx="12" cy="12" rx="4" ry="9"/><path d="M3 12h18M5 7h14M5 17h14"/></svg>
        <span class="contact__web">www.ferrolane.com.au</span>
      </div>
    </div>
  </section>
</div>
</body>
</html>
```